KestrelHollowCo.com

I need a site that I can sell dewatering equipment to the construction industry.
Ie, pipes fittings pumps and other such things needed to remove the groundwater on construction sites. Here in Florida, it’s needed almost everywhere seeing we are at sea level.
I want to be able to sell these products on the site and receive

```html
<!DOCTYPE html>
<html lang="en">
<head>
<meta charset="utf-8">
<title>Kestrel Hollow Co — Dewatering Equipment</title>
<link href="https://fonts.googleapis.com/css2?family=Lato:wght@400;700;900&display=swap" rel="stylesheet">
<style>
:root{
  --ink:#1b2836;
  --ink-deep:#141d27;
  --panel:#1f2c3a;
  --blue:#2f8fdc;
  --blue-soft:#4aa3e6;
  --white:#ffffff;
  --muted:#aeb8c3;
  --text:#333a42;
  --card-bg:#eaf3fb;
}
*{box-sizing:border-box;margin:0;padding:0}
html,body{width:1200px;height:3758px;overflow:hidden}
body{position:relative;font-family:"Lato",Arial,sans-serif;color:var(--text);background:var(--white)}
.abs{position:absolute}

/* top bar */
.topbar{left:0;top:0;width:1200px;height:22px;background:var(--ink-deep);color:var(--white);font-size:9px}
.topbar .addr{position:absolute;left:248px;top:0;height:22px;display:flex;align-items:center;gap:6px}
.topbar .quote{position:absolute;left:800px;top:0;height:22px;padding:0 12px;line-height:22px}
.topbar .phone{position:absolute;left:862px;top:0;height:22px;padding:0 16px;line-height:22px;background:var(--blue)}

/* hero */
.hero{left:0;top:22px;width:1200px;height:576px;background:linear-gradient(180deg,#6fa6d6 0%,#b9d3ea 38%,#cfdbe0 52%,#5f8b8c 66%,#4f7a3a 82%,#7aa24a 100%);border-bottom:4px solid var(--blue)}
.brand{left:240px;top:38px;width:140px;text-align:center;color:var(--blue);font-weight:900;font-size:14px;letter-spacing:.3px;line-height:1.1}
.brand .dot{display:block;width:34px;height:34px;border-radius:50%;background:var(--blue);margin:0 auto 6px}
.nav{left:608px;top:58px;display:flex;gap:22px;align-items:center;font-size:12px;color:#1c2a38}
.nav .active{font-weight:700}
.nav .contact{background:var(--white);padding:7px 10px;border:1px solid #d0d6dc;margin-left:-6px}
.hero-copy{left:350px;top:262px;width:500px;text-align:center}
.hero-copy h1{font-size:27px;font-weight:700;color:#1b2836;margin-bottom:6px}
.hero-copy p{font-size:15px;line-height:1.25;color:#1b2836}
.btn{display:inline-block;font-size:12px;color:var(--white);text-align:center;line-height:38px;height:38px}
.hero-btns{left:482px;top:394px;display:flex;gap:18px}
.hero-btns .btn{width:112px}
.btn-blue{background:var(--blue-soft)}
.btn-dark{background:var(--ink)}

/* feature cards */
.feature{top:566px;width:266px;height:236px;box-shadow:0 4px 10px rgba(0,0,0,.35);overflow:hidden}
.feature .photo{position:absolute;inset:0}
.feature .label{position:absolute;left:0;bottom:0;width:100%;height:56px;background:rgba(20,29,39,.82);color:var(--white);font-size:12px;display:flex;align-items:center;gap:10px;padding-left:16px}
.feature.open .label{top:0;height:auto;bottom:0;background:rgba(20,29,39,.78);align-items:flex-start;flex-direction:column;padding:120px 18px 0 70px;gap:6px}
.feature.open .label b{font-weight:400;font-size:12px}
.feature.open .label span{font-size:9px;line-height:1.35;color:#dbe2e8}
.feature .ico{width:22px;height:22px}

/* services */
.services{left:0;top:859px;width:1200px;height:474px;background:var(--ink)}
.section-title{font-size:20px;font-weight:700;text-align:center}
.services .section-title{color:var(--white);margin-top:50px}
.services .grid{position:absolute;left:200px;top:124px;width:800px;display:grid;grid-template-columns:repeat(3,1fr);row-gap:30px}
.service{text-align:center;color:var(--white)}
.service svg{width:40px;height:40px;stroke:var(--white);fill:none;stroke-width:2}
.service h3{color:var(--blue-soft);font-weight:400;font-size:13px;margin:8px 0 6px}
.service p{font-size:9px;line-height:1.45;width:160px;margin:0 auto}
.service .more{font-size:9px;color:var(--muted);margin-top:6px}

/* banner */
.banner{left:0;top:1333px;width:1200px;height:298px;background:radial-gradient(ellipse at 30% 60%,#2d7f93 0%,#1d4d5c 35%,#4d4a40 70%,#3a3a36 100%)}
.banner-copy{left:330px;top:1389px;width:540px;text-align:center;color:var(--white)}
.banner-copy h2{font-size:27px;font-weight:700;margin-bottom:12px}
.banner-copy p{font-size:11px;line-height:1.45}
.banner-btn{left:544px;top:1531px;width:112px;background:var(--blue-soft)}

/* projects */
.projects{left:0;top:1631px;width:1200px;height:573px;background:linear-gradient(180deg,#3b8fd6 0%,#3a95e0 100%)}
.projects .section-title{color:var(--white);margin-top:56px}
.filters{position:absolute;left:0;top:118px;width:1200px;display:flex;justify-content:center;gap:20px;font-size:9px;color:#0f2238}
.tiles{position:absolute;left:195px;top:165px;display:grid;grid-template-columns:repeat(4,191px);grid-auto-rows:163px;column-gap:14px;row-gap:15px}
.tile{background:var(--panel);color:var(--blue-soft);font-size:15px;display:flex;align-items:center;justify-content:center}

/* news */
.news{left:0;top:2204px;width:1200px;height:539px;background:var(--white)}
.news .section-title{color:#1b2836;margin-top:52px}
.post{position:absolute;top:133px;width:256px;height:338px;background:var(--card-bg);border-left:3px solid var(--blue)}
.post .photo{height:146px}
.post h4{color:var(--blue-soft);font-weight:400;font-size:13px;margin:20px 0 0 16px}
.post .meta{font-size:8px;color:#555;margin:10px 0 0 16px}
.post p{font-size:9px;line-height:1.55;margin:22px 16px 0 16px}
.post .more{font-size:9px;color:var(--blue);margin:6px 0 0 16px}
.dots{position:absolute;left:578px;top:498px;display:flex;gap:5px}
.dots i{width:7px;height:7px;border-radius:50%;background:#c9d0d7}
.dots i:first-child{background:var(--blue)}

/* map */
.map{left:0;top:2743px;width:1200px;height:338px;background:linear-gradient(135deg,#e3e4e5,#cfd0d2 60%,#dcdddf)}

/* footer */
.footer{left:0;top:3081px;width:1200px;height:501px;background:linear-gradient(180deg,#22303d,#2b3a46 50%,#1c2934)}
.footer h3{color:var(--white);font-size:24px;font-weight:700}
.about{left:245px;top:38px;width:300px;color:var(--white)}
.about p{font-size:9px;line-height:1.4;margin-top:6px}
.about .ql{margin-top:14px}
.links{display:grid;grid-template-columns:90px 90px;row-gap:4px;font-size:9px;margin-top:10px}
.contacts{left:245px;top:260px;color:var(--white);font-size:12px}
.contacts div{display:flex;align-items:center;gap:10px;margin-bottom:12px}
.contacts em{font-style:normal;color:var(--blue-soft)}
.contacts svg{width:18px;height:18px;fill:var(--white)}
.social{left:245px;top:390px;display:flex;gap:26px;align-items:center}
.social i{width:30px;height:30px;border-radius:50%;background:var(--white);display:block}
.social i.hl{background:var(--blue-soft);width:42px;height:42px}
.connect{left:245px;top:446px;font-size:9px;letter-spacing:4px;color:var(--white)}
.contact-form{left:610px;top:38px;width:336px}
.contact-form .field{height:36px;border:1px solid #c7d0d8;margin-top:12px;font-size:6px;color:#dbe2e8;padding:13px 10px}
.contact-form .msg{height:84px}
.contact-form .check{margin-top:16px;width:198px;height:48px;background:#f2f2f2;border:1px solid #ccc}
.contact-form .send{margin-top:16px;width:78px;height:28px;line-height:28px;background:var(--blue);color:var(--white);font-size:10px;text-align:center}

/* bottom */
.bottom{left:0;top:3582px;width:1200px;height:176px;background:var(--ink-deep);text-align:center;color:var(--white)}
.bottom .brand{position:static;width:auto;margin:34px auto 0;color:var(--white);font-size:16px}
.bottom .brand .dot{background:var(--white)}
.bottom .legal{font-size:7px;margin-top:18px;letter-spacing:.3px}
</style>
</head>
<body>

<div class="abs topbar">
  <span class="addr"><svg width="9" height="11" viewBox="0 0 10 14"><path d="M5 0a5 5 0 0 0-5 5c0 4 5 9 5 9s5-5 5-9a5 5 0 0 0-5-5zm0 7a2 2 0 1 1 0-4 2 2 0 0 1 0 4z" fill="#fff"/></svg>ABC Street City 12345</span>
  <span class="quote">Get a Quote</span>
  <span class="phone">(000) 000-0000</span>
</div>

<header class="abs hero" role="img" aria-label="Photo of an industrial building beside a canal with a large pipe running along a grassy bank"></header>
<div class="abs brand"><span class="dot"></span>Kestrel Hollow Co</div>
<nav class="abs nav"><span class="active">Home</span><span>About</span><span>Services</span><span>Projects</span><span>News</span><span class="contact">Contact Us</span></nav>
<div class="abs hero-copy">
  <h1>Welcome to Kestrel Hollow</h1>
  <p>Lorem Ipsum has been the industry's standard dummy text ever since the 1500s, when an unknown printer took a galley of type and scrambled it to make a type specimen book.</p>
</div>
<div class="abs hero-btns"><span class="btn btn-blue">Explore</span><span class="btn btn-dark">Buy Now</span></div>

<div class="abs feature" style="left:193px">
  <div class="photo" role="img" aria-label="Photo of a construction dewatering excavation" style="background:linear-gradient(160deg,#7a6a52,#4b4030 60%,#2f3a42)"></div>
  <div class="label"><svg class="ico" viewBox="0 0 24 24" fill="none" stroke="#4aa3e6" stroke-width="2"><path d="M12 2v20M5 8h14M7 22h10"/></svg>Construction Dewatering</div>
</div>
<div class="abs feature open" style="left:468px">
  <div class="photo" role="img" aria-label="Photo of pumps and equipment on site" style="background:linear-gradient(160deg,#8a7658,#5c4c38)"></div>
  <div class="label"><b>Pumps and Equipment Rental</b><span>Lorem Ipsum has been the industry's standard dummy text ever since the 1500s, when an unknown printer took a galley of type and scrambled it to make a type specimen book.</span></div>
  <svg class="abs" style="left:20px;top:118px" width="26" height="26" viewBox="0 0 24 24" fill="#4aa3e6"><circle cx="12" cy="12" r="3"/><path d="M12 2l3 7h-6zM22 12l-7 3v-6zM12 22l-3-7h6zM2 12l7-3v6z"/></svg>
</div>
<div class="abs feature" style="left:741px">
  <div class="photo" role="img" aria-label="Photo of bypass pumping pipes laid across a yard" style="background:linear-gradient(180deg,#8db7d8,#6b8a4c 45%,#8f8a78)"></div>
  <div class="label"><svg class="ico" viewBox="0 0 24 24" fill="#4aa3e6"><rect x="3" y="12" width="4" height="9"/><rect x="10" y="7" width="4" height="14"/><rect x="17" y="3" width="4" height="18"/></svg>Bypass Pumping</div>
</div>

<section class="abs services">
  <h2 class="section-title">Services</h2>
  <div class="grid">
    <div class="service"><svg viewBox="0 0 40 40"><rect x="6" y="14" width="24" height="14" rx="3"/><circle cx="12" cy="32" r="3"/><circle cx="26" cy="32" r="3"/><path d="M30 20h6"/></svg><h3>Pumping Services</h3><p>Lorem Ipsum is simply dummy text of the printing and typesetting industry.</p><div class="more">Read More</div></div>
    <div class="service"><svg viewBox="0 0 40 40"><path d="M20 4v32M12 10l8 6 8-6M8 36h24M14 22h12"/></svg><h3>Dewatering</h3><p>Lorem Ipsum is simply dummy text of the printing and typesetting industry.</p><div class="more">Read More</div></div>
    <div class="service"><svg viewBox="0 0 40 40"><path d="M8 34h24M14 34V18a8 8 0 0 1 16 0M22 10l6-6"/></svg><h3>One-Pass Trenching</h3><p>Lorem Ipsum is simply dummy text of the printing and typesetting industry.</p><div class="more">Read More</div></div>
    <div class="service"><svg viewBox="0 0 40 40"><circle cx="20" cy="20" r="12"/><path d="M22 10l-6 11h8l-6 10"/></svg><h3>Power Generation</h3><p>Lorem Ipsum is simply dummy text of the printing and typesetting industry.</p><div class="more">Read More</div></div>
    <div class="service"><svg viewBox="0 0 40 40"><rect x="10" y="8" width="20" height="28"/><path d="M10 16h20M16 4h8"/></svg><h3>Water Filtration &amp; Treatment</h3><p>Lorem Ipsum is simply dummy text of the printing and typesetting industry.</p><div class="more">Read More</div></div>
    <div class="service"><svg viewBox="0 0 40 40"><path d="M20 4v32M14 10h12M12 18l16 4M12 26l16 4"/></svg><h3>Drilling</h3><p>Lorem Ipsum is simply dummy text of the printing and typesetting industry.</p><div class="more">Read More</div></div>
  </div>
</section>

<section class="abs banner" role="img" aria-label="Aerial photo of a coastline with blue water and land"></section>
<div class="abs banner-copy">
  <h2>Lorem Ipsum is Simply Dummy</h2>
  <p>Lorem Ipsum is simply dummy text of the printing and typesetting industry. Lorem Ipsum has been the industry's standard dummy text ever since the 1500s, when an unknown printer took a galley of type and scrambled it to make a type specimen book. It has survived not only five centuries, but also the leap into electronic typesetting, remaining essentially unchanged.</p>
</div>
<span class="abs btn banner-btn">Get a Quote</span>

<section class="abs projects">
  <h2 class="section-title">Recent Projects</h2>
  <div class="filters"><span>All Projects</span><span>Pumping Services</span><span>Dewatering</span><span>One-Pass Trenching</span><span>Power Generation</span><span>Water Filtration &amp; Treatment</span></div>
  <div class="tiles">
    <div class="tile">image</div><div class="tile">image</div><div class="tile">image</div><div class="tile">image</div>
    <div class="tile">image</div><div class="tile">image</div><div class="tile">image</div><div class="tile">image</div>
  </div>
</section>

<section class="abs news">
  <h2 class="section-title">Recent News</h2>
  <article class="post" style="left:195px"><div class="photo" role="img" aria-label="Photo of friends at sunset" style="background:linear-gradient(180deg,#e8c08a,#b0855a)"></div><h4>Lorem Ipsum is simply</h4><div class="meta">June 4, 2018 &nbsp;|&nbsp; 0 Comments</div><p>Lorem Ipsum is simply dummy text of the printing and typesetting industry. Lorem Ipsum has been the industry's standard dummy text ever since the 1500s, when an unknown printer took a galley of type and</p><div class="more">Read More</div></article>
  <article class="post" style="left:476px"><div class="photo" role="img" aria-label="Photo of joined hands in teamwork" style="background:linear-gradient(180deg,#eef0f2,#c8b8a8)"></div><h4>Lorem Ipsum is simply</h4><div class="meta">June 4, 2018 &nbsp;|&nbsp; 0 Comments</div><p>Lorem Ipsum is simply dummy text of the printing and typesetting industry. Lorem Ipsum has been the industry's standard dummy text ever since the 1500s, when an unknown printer took a galley of type and</p><div class="more">Read More</div></article>
  <article class="post" style="left:751px"><div class="photo" role="img" aria-label="Photo of a desk with laptop and papers" style="background:linear-gradient(180deg,#a88466,#d9d6d0)"></div><h4>Lorem Ipsum is simply</h4><div class="meta">June 4, 2018 &nbsp;|&nbsp; 0 Comments</div><p>Lorem Ipsum is simply dummy text of the printing and typesetting industry. Lorem Ipsum has been the industry's standard dummy text ever since the 1500s, when an unknown printer took a galley of type and</p><div class="more">Read More</div></article>
  <div class="dots"><i></i><i></i><i></i><i></i></div>
</section>

<section class="abs map" role="img" aria-label="Grey street map of the business location"></section>

<footer class="abs footer">
  <div class="abs about">
    <h3>About</h3>
    <p>Lorem Ipsum has been the industry's standard dummy text ever since the 1500s, when an unknown printer took a galley of type and scrambled it to make a type specimen book.</p>
    <h3 class="ql">Quick Links</h3>
    <div class="links"><span>Home</span><span>Project</span><span>About Us</span><span>News</span><span>Services</span><span>Contact Us</span></div>
  </div>
  <div class="abs contacts">
    <div><svg viewBox="0 0 10 14"><path d="M5 0a5 5 0 0 0-5 5c0 4 5 9 5 9s5-5 5-9a5 5 0 0 0-5-5zm0 7a2 2 0 1 1 0-4 2 2 0 0 1 0 4z"/></svg><em>Address:</em> ABC Street City 12345</div>
    <div><svg viewBox="0 0 24 24"><path d="M6 2l4 4-2 3c1 3 4 6 7 7l3-2 4 4-3 4C10 22 2 14 2 5z"/></svg><em>Phone:</em> (000) 000 - 0000</div>
    <div><svg viewBox="0 0 24 18"><path d="M0 0h24v18H0zM2 2l10 8 10-8v2l-10 8L2 4z" fill-rule="evenodd"/></svg><em>Email:</em> info@mysite.com</div>
  </div>
  <div class="abs social"><i></i><i class="hl"></i><i></i></div>
  <div class="abs connect">CONNECT WITH US</div>
  <div class="abs contact-form">
    <h3>Contact Us</h3>
    <div class="field">YOUR NAME (REQUIRED)</div>
    <div class="field">YOUR EMAIL (REQUIRED)</div>
    <div class="field">SUBJECT</div>
    <div class="field">DATE OF PURCHASE</div>
    <div class="field msg">YOUR MESSAGE</div>
    <div class="check"></div>
    <div class="send">Send</div>
  </div>
</footer>

<div class="abs bottom">
  <div class="brand"><span class="dot"></span>Kestrel Hollow Co</div>
  <div class="legal">COPYRIGHT © 2018 KESTREL HOLLOW CO. ALL RIGHTS RESERVED.</div>
</div>

</body>
</html>
```